Carpet cleaning company wants business card

Need an exciting new fresh design for business cards for my carpet cleaning /pest control business
www.tidewellhomecare.com.au
Can design include a lined section for quoting or information? Thanks !

```html
<!DOCTYPE html>
<html lang="en">
<head>
<meta charset="utf-8">
<title>Tidewell Home Care – Business Card</title>
<link href="https://fonts.googleapis.com/css2?family=Inter:wght@400;700&display=swap" rel="stylesheet">
<style>
  :root {
    --brand-blue: #0d58a6;
    --brand-red: #e8383d;
    --ink: #4a4a4a;
    --rule: #cfcfcf;
    --paper: #ffffff;
    --backdrop: #e4e4e4;
  }
  * { box-sizing: border-box; margin: 0; padding: 0; }
  html, body { width: 1200px; height: 1040px; overflow: hidden; }
  body {
    background: var(--backdrop);
    font-family: "Inter", Arial, sans-serif;
    position: relative;
  }
  .card {
    position: absolute;
    width: 642px;
    height: 367px;
    border-radius: 16px;
    overflow: hidden;
  }
  .card-front { left: 285px; top: 130px; background: var(--paper); }
  .card-back { left: 284px; top: 568px; background: var(--brand-blue); }

  .wordmark {
    position: absolute;
    font-weight: 700;
    letter-spacing: -0.5px;
    white-space: nowrap;
  }
  .card-front .wordmark {
    right: 41px;
    top: 62px;
    font-size: 36px;
    color: var(--brand-blue);
  }
  .card-back .wordmark {
    left: 0; right: 0;
    top: 154px;
    text-align: center;
    font-size: 50px;
    color: var(--paper);
  }

  .holder {
    position: absolute;
    left: 42px;
    top: 190px;
  }
  .holder-name {
    font-size: 26px;
    font-weight: 700;
    color: var(--brand-blue);
    line-height: 1.1;
  }
  .holder-title {
    font-size: 14px;
    color: var(--brand-red);
    margin-top: 2px;
  }
  .divider {
    position: absolute;
    left: 42px;
    width: 559px;
    top: 248px;
    height: 1px;
    background: var(--rule);
  }
  .contacts {
    position: absolute;
    left: 42px;
    top: 256px;
    list-style: none;
  }
  .contacts li {
    display: flex;
    align-items: center;
    height: 19px;
    font-size: 15px;
    color: var(--ink);
  }
  .contacts svg {
    width: 14px; height: 14px;
    margin-right: 9px;
    fill: var(--brand-blue);
    flex: none;
  }
  .edge-line-blue {
    position: absolute; left: 2px; width: 484px; top: 354px; height: 2px;
    background: var(--brand-blue);
  }
  .edge-line-red {
    position: absolute; left: 491px; right: 2px; top: 353px; height: 2px;
    background: var(--brand-red);
  }
  .edge-band {
    position: absolute; left: 0; right: 0; top: 357px; bottom: 0;
    background: var(--brand-blue);
  }
</style>
</head>
<body>

<section class="card card-front">
  <div class="wordmark">Tidewell Home Care</div>

  <div class="holder">
    <div class="holder-name">Daniel Reyes</div>
    <div class="holder-title">President</div>
  </div>

  <div class="divider"></div>

  <ul class="contacts">
    <li>
      <svg viewBox="0 0 16 16" aria-hidden="true"><path d="M3.6 1.2l2.3 2.6-1.2 1.9c.9 2 2.6 3.7 4.6 4.6l1.9-1.2 2.6 2.3-1.3 2.3C7 13.3 2.7 9 1.3 2.5z"/></svg>
      07 5123 4400
    </li>
    <li>
      <svg viewBox="0 0 16 16" aria-hidden="true"><path d="M4 0h8a1 1 0 0 1 1 1v14a1 1 0 0 1-1 1H4a1 1 0 0 1-1-1V1a1 1 0 0 1 1-1zm.8 2v10.5h6.4V2z"/></svg>
      0412 555 019
    </li>
    <li>
      <svg viewBox="0 0 16 16" aria-hidden="true"><path d="M1 4h14v9H1zm1.5 1.2v.4L8 9.4l5.5-3.8v-.4L8 8.4z"/></svg>
      admin@tidewellhomecare.com.au
    </li>
    <li>
      <svg viewBox="0 0 16 16" aria-hidden="true"><circle cx="8" cy="8" r="7"/><path d="M5 4.5c1.5.5 2 1.5 1.5 2.7-.6 1 .4 2 1.6 2.1.8.3.6 1.8-.2 3.2M10.5 3.5c-.5 1 .3 1.8 1.5 1.7" stroke="#fff" stroke-width="1.3" fill="none"/></svg>
      www.tidewellhomecare.com.au
    </li>
  </ul>

  <div class="edge-line-blue"></div>
  <div class="edge-line-red"></div>
  <div class="edge-band"></div>
</section>

<section class="card card-back">
  <div class="wordmark">Tidewell Home Care</div>
</section>

</body>
</html>
```